Health Care Company with Logo Needs Business Cards designed

We are a luxury behavioral health company looking for business cards design we already have a logo and are looking for someone to design a sophisticated luxurious looking business card. Please note that Card design should be captivating just like the logo and also encompass the logo color

Industry/Entity Type

Healthcare

Contact Information for Business Card

Logo,company name, tagline, my name and title, contact details, and physical address

```html
<!DOCTYPE html>
<html lang="en">
<head>
<meta charset="utf-8">
<title>Norvale Behavioral Health – Business Card</title>
<link rel="stylesheet" href="https://fonts.googleapis.com/css2?family=Arimo:wght@400;700&display=swap">
<style>
  :root {
    --purple: #7b3a99;
    --purple-deep: #6a2d88;
    --blue: #29a7df;
    --green: #8cc63f;
    --orange: #f7941d;
    --ink: #231f20;
    --paper: #ffffff;
    --stage: #2a2a2c;
  }
  * { margin: 0; padding: 0; box-sizing: border-box; }
  html, body {
    width: 1200px; height: 900px; overflow: hidden;
    background: var(--stage);
    font-family: "Arimo", Arial, sans-serif;
  }
  .stage {
    position: relative; width: 1200px; height: 900px;
  }
  .card {
    position: absolute; left: 250px; width: 700px; height: 400px;
    border-radius: 26px; overflow: hidden;
  }
  /* ---------- front ---------- */
  .card-front { top: 40px; background: var(--paper); }
  .brand {
    position: absolute; left: 150px; top: 38px;
    font-size: 40px; font-weight: 700; color: var(--purple);
    letter-spacing: -0.5px;
  }
  .tagline {
    position: absolute; left: 140px; top: 88px;
    font-size: 12px; font-weight: 700; color: var(--blue);
    letter-spacing: 3.2px; text-transform: uppercase;
  }
  .accent-bar {
    position: absolute; left: 44px; top: 128px;
    width: 14px; height: 40px; background: var(--orange);
  }
  .person-name {
    position: absolute; left: 72px; top: 126px;
    font-size: 32px; font-weight: 700; color: var(--purple);
    letter-spacing: 1px; text-transform: uppercase;
  }
  .person-title {
    position: absolute; left: 72px; top: 166px;
    font-size: 20px; color: var(--ink);
  }
  .address {
    position: absolute; left: 72px; top: 208px;
    font-size: 19px; line-height: 26px; color: var(--ink);
    font-style: normal;
  }
  .contact-list {
    position: absolute; left: 56px; top: 266px; list-style: none;
    font-size: 19px; line-height: 28px; color: var(--ink);
  }
  .contact-list li { display: flex; align-items: center; gap: 8px; }
  .contact-list svg { width: 16px; height: 16px; fill: var(--blue); flex: none; }
  .card-band {
    position: absolute; left: 0; bottom: 0; width: 700px; height: 80px;
  }
  .website {
    position: absolute; right: 34px; bottom: 16px;
    font-size: 19px; color: var(--paper); letter-spacing: 0.3px;
  }
  /* ---------- back ---------- */
  .card-back { top: 460px; background: var(--purple); }
  .back-pattern {
    position: absolute; inset: 0;
    background: linear-gradient(135deg, var(--purple) 0%, var(--purple-deep) 50%, var(--purple) 100%);
  }
  .back-lockup {
    position: absolute; left: 50px; bottom: 56px;
    display: flex; align-items: center; gap: 14px;
  }
  .back-mark { width: 34px; height: 34px; background: var(--orange); flex: none; }
  .back-brand { font-size: 36px; font-weight: 700; color: var(--paper); letter-spacing: -0.5px; }
  .back-tagline {
    position: absolute; left: 98px; bottom: 36px;
    font-size: 11px; font-weight: 700; color: var(--blue);
    letter-spacing: 3px; text-transform: uppercase;
  }
</style>
</head>
<body>
<main class="stage">

  <section class="card card-front" aria-label="Business card front">
    <div class="brand">Norvale Behavioral Health</div>
    <div class="tagline">Dedicated to hope, healing and recovery</div>

    <span class="accent-bar"></span>
    <h1 class="person-name">Daniel Whitford</h1>
    <p class="person-title">Founder &amp; CEO</p>
    <address class="address">2280 Harbor Glen Ave Suite 410<br>Maple Ridge, TN 37815</address>

    <ul class="contact-list">
      <li>
        <svg viewBox="0 0 16 16" aria-hidden="true"><path d="M4 1c1 0 2 3 2 4s-1 1.5-1 2 2.5 3.5 4 4 1-1 2-1 4 1 4 2-1 3-3 3C6 15 1 10 1 4c0-2 2-3 3-3z"/></svg>
        555-014-2290
      </li>
      <li>
        <svg viewBox="0 0 16 16" aria-hidden="true"><path d="M4 1h8v4H4zM1 6h14v6h-3v3H4v-3H1zM5 10v4h6v-4z"/></svg>
        555-017-6634
      </li>
      <li>
        <svg viewBox="0 0 16 16" aria-hidden="true"><path d="M1 3h14v1L8 9 1 4zM1 6l7 5 7-5v7H1z"/></svg>
        hello@norvalebehavioral.com
      </li>
    </ul>

    <svg class="card-band" viewBox="0 0 700 80" preserveAspectRatio="none" aria-hidden="true">
      <rect x="0" y="36" width="180" height="6" fill="var(--blue)"/>
      <rect x="180" y="36" width="170" height="6" fill="var(--green)"/>
      <path d="M350 36 H520 C538 36 546 14 566 14 H700 V20 H568 C552 20 544 42 522 42 H350 Z" fill="var(--orange)"/>
      <path d="M0 48 H524 C548 48 552 26 572 26 H700 V80 H0 Z" fill="var(--purple)"/>
    </svg>
    <div class="website">www.norvalebehavioral.com</div>
  </section>

  <section class="card card-back" aria-label="Business card back">
    <div class="back-pattern" role="img" aria-label="Repeating tonal brand pattern on purple"></div>
    <div class="back-lockup">
      <span class="back-mark"></span>
      <span class="back-brand">Norvale Behavioral Health</span>
    </div>
    <div class="back-tagline">Dedicated to hope, healing and recovery</div>
  </section>

</main>
</body>
</html>
```